Bramble Hollow is company name.Handknit&crochet blankets&scarves. Need logo&business ...

I need a design that is eye catching, using yarn and is flowing. I'd like to see colors in aqua (Halvorsen Pike paint HP4817 Merilune) for the yarn and company name. For the text, a dark grey color (Halvorsen Pike HP5308 Velden Ash)

Colors
87cfc7

```html
<!DOCTYPE html>
<html lang="en">
<head>
<meta charset="utf-8">
<title>Bramble Hollow – Business Cards</title>
<link href="https://fonts.googleapis.com/css2?family=Jost:wght@400;500;600&display=swap" rel="stylesheet">
<style>
  :root{
    --merilune:#87cfc7;
    --merilune-deep:#7cc6bc;
    --velden-ash:#4b4f52;
    --paper:#f7f8f8;
    --backdrop:#b9bcc1;
    --white:#ffffff;
  }
  *{box-sizing:border-box;margin:0;padding:0}
  html,body{width:1200px;height:675px;overflow:hidden}
  body{
    background:var(--backdrop);
    font-family:"Jost",sans-serif;
    position:relative;
  }
  .card{
    position:absolute;top:189px;width:520px;height:297px;
    border-radius:4px;overflow:hidden;
    box-shadow:0 10px 28px rgba(40,45,55,.25);
  }
  .card-back{left:50px;background:var(--merilune)}
  .card-front{left:630px;background:var(--paper)}
  .card svg.thread{position:absolute;inset:0}

  /* back */
  .care-list{
    position:absolute;left:300px;top:112px;list-style:none;
    color:var(--white);font-size:13px;letter-spacing:.4px;
  }
  .care-list li{display:flex;align-items:center;gap:10px;height:19px}
  .care-list svg{width:18px;height:14px;flex:none}
  .brand-mark{
    position:absolute;display:flex;align-items:center;gap:8px;
    font-weight:400;white-space:nowrap;
  }
  .card-back .brand-mark{left:34px;bottom:30px;color:var(--white);font-size:22px}
  .card-back .brand-mark .dot{width:14px;height:14px;border-radius:50%;background:var(--white)}

  /* front */
  .card-front .brand-mark{left:120px;top:60px;color:var(--merilune-deep);font-size:40px;background:var(--paper);padding:0 10px}
  .card-front .brand-mark .dot{width:26px;height:26px;border-radius:50%;background:var(--merilune-deep)}
  .contact{position:absolute;left:40px;top:190px;color:var(--velden-ash)}
  .contact .person{font-weight:600;font-size:17px;letter-spacing:2px;margin-bottom:8px}
  .contact p{display:flex;align-items:center;gap:10px;font-size:14px;height:22px}
  .contact .icon{width:18px;height:18px;border-radius:50%;background:var(--velden-ash);display:flex;align-items:center;justify-content:center}
  .contact .icon svg{width:11px;height:11px}
  .divider{position:absolute;left:292px;top:158px;width:6px;height:92px;border-left:1px solid var(--velden-ash);border-right:1px solid var(--velden-ash)}
  .services{position:absolute;left:322px;top:166px;list-style:none;color:var(--velden-ash);font-size:13px;font-weight:500;letter-spacing:.3px;line-height:19px}
</style>
</head>
<body>

<section class="card card-back" aria-label="Card back">
  <svg class="thread" viewBox="0 0 520 297" aria-hidden="true">
    <path d="M0 142 C60 132 120 126 170 112 C220 98 230 60 300 54 C360 48 390 56 400 34 C410 8 440 4 520 4" fill="none" stroke="#fff" stroke-width="2"/>
  </svg>
  <ul class="care-list">
    <li><svg viewBox="0 0 18 14"><path d="M1 5h16l-2 8H3z M4 5 6 1 9 5 12 1 14 5" fill="none" stroke="#fff" stroke-width="1.4"/></svg>HAND WASH</li>
    <li><svg viewBox="0 0 18 14"><path d="M9 1 17 13H1z" fill="none" stroke="#fff" stroke-width="1.4"/></svg>BLEACHING ALLOWED</li>
    <li><svg viewBox="0 0 18 14"><rect x="2" y="1" width="14" height="12" fill="none" stroke="#fff" stroke-width="1.4"/><path d="M5 7h8" stroke="#fff" stroke-width="1.4"/></svg>DRY FLAT</li>
    <li><svg viewBox="0 0 18 14"><rect x="2" y="1" width="14" height="12" fill="none" stroke="#fff" stroke-width="1.4"/><circle cx="9" cy="7" r="4" fill="none" stroke="#fff" stroke-width="1.2"/><path d="M2 1l14 12M16 1 2 13" stroke="#fff" stroke-width="1.4"/></svg>DO NOT TUMBLE DRY</li>
    <li><svg viewBox="0 0 18 14"><path d="M2 12h14l-2-8H6z" fill="none" stroke="#fff" stroke-width="1.4"/><path d="M3 2l12 11M15 2 3 13" stroke="#fff" stroke-width="1.4"/></svg>DO NOT IRON</li>
  </ul>
  <div class="brand-mark"><span class="dot"></span>Bramble Hollow</div>
</section>

<section class="card card-front" aria-label="Card front">
  <svg class="thread" viewBox="0 0 520 297" aria-hidden="true">
    <path d="M0 82 C60 72 110 70 140 82 M420 80 C450 78 460 50 480 42 C495 36 505 34 520 34" fill="none" stroke="var(--merilune-deep)" stroke-width="2.5"/>
  </svg>
  <div class="brand-mark"><span class="dot"></span>Bramble Hollow</div>

  <div class="contact">
    <h2 class="person">INGRID MOLL</h2>
    <p><span class="icon"><svg viewBox="0 0 12 12"><path d="M2 1h3l1 3-2 1a7 7 0 0 0 3 3l1-2 3 1v3c-6 0-10-4-9-9z" fill="#fff"/></svg></span>+63-2-8000-0199</p>
    <p><span class="icon"><svg viewBox="0 0 12 12"><rect x="1" y="3" width="10" height="7" fill="#fff"/><path d="M1 3l5 4 5-4" fill="none" stroke="#4b4f52" stroke-width="1"/></svg></span>ingridmoll@example.com</p>
  </div>

  <div class="divider"></div>

  <ul class="services">
    <li>HAND KNIT &amp; CROCHET</li>
    <li>BABY AFGHANS</li>
    <li>AFGHANS</li>
    <li>SCARVES, GLOVES, HATS</li>
  </ul>
</section>

</body>
</html>
```